Need a clean & modern homepage for an education site + opportunity for longer term work

Thanks for viewing our project. We are excited about this new website and we hope that we might build a relationship with designers as we work on this project. I provided quite a few details and requirements to help you more quickly create a design that meets our needs.
Who we are:
We are a website that discusses the importance of college accreditation and provides a directory of college programs.
What we need:
A homepage that meets the below requirements and is inspired by the examples provided
Definition of accredited:
ac·cred·it·ed [uh-kred-i-tid] adj.
1. officially recognized as meeting the essential requirements, as of academic excellence: accredited schools.
2. provided with official credentials, as by a government: an accredited diplomatic representative.
3. accepted as authoritative: an accredited theory.
Overall look and feel for the homepage:
- Clean, simple and modern
- Limited (or zero) pictures
- Utilize color blocks with text
- A trend seems to be longer vertical length homepages with lots of whitespace. I generally like this trend as long as the page is not way to tall.
Inspirations: Sites that have a similar look and feel to what I need.
http://plinvar.org/
http://www.tumbrelstat.com/colleges/harrowgate-university/
http://quietmarble.org/
http://www.vellichorstaffing.com/
http://www.plonk.com/
http://sketches.zimvo.com/
Items to be included on the homepage. Details below on each item.
- Top navigation
- Logo: Please leave a blank area for a logo. The logo has not been designed.
- Simple graphic/color block at the top that highlights a definition of “Accredited” – the definition should be formatted like it is being copy/pasted from a dictionary.
- Space for a video and small (50 word) written description of the video. You can use placeholder text.
- One section with 3 Paragraphs of content (each paragraph around 100 words) with a header at the top. You can use placeholder text but please create the formatting. At the end of the 3 paragraphs please have a “Read More” Note this shouldn't be 3 separate paragraphs with three read mores - it is 3 paragraphs with one read more at the end.
- An area with the header “Search Colleges by State” that has anchor text links to all 50 states.
Top navigation:
- Home
- States – with a subnav dropdown that includes all 50 US states.
- Programs – with a subnav dropdown that includes program titles (list below)
- Degrees - with a subnav dropdown that includes 5 degree levels (list below)
- Accreditation – no subnav
- Rankings – no subnav
- Resources – no subnav
Footer
- Link to about us, privacy, and a copyright www.url.com
Programs List for sub navigation
Accounting
Art
Bible
Business
Criminal Justice
Design
Engineering
English
Law
LPN to RN
Management
Math
MBA
MPH
Medical Assisting
Military
Nursing
Occupational Therapy
Paralegal
Psychology
Pharmacy
RN to BSN
Radiology
Social Work
Sonography
Degrees list for sub navigation
Certificate
Associate
Bachelors
Masters
PhD
Thanks so much - looking forward to working with you!

```html
<!DOCTYPE html>
<html lang="en">
<head>
<meta charset="utf-8">
<title>Accredited – Homepage</title>
<link rel="stylesheet" href="https://fonts.googleapis.com/css2?family=Lato:ital,wght@0,400;0,700;1,700&family=Tinos:ital,wght@0,400;0,700;1,400&display=swap">
<style>
  :root {
    --topbar: #e6e6e6;
    --white: #ffffff;
    --brand-blue: #1ea6e2;
    --nav-active: #29a8e0;
    --text: #4a4a4a;
    --text-dark: #222222;
    --dropdown: #e2e2e2;
    --hero-dark: #5b8fc4;
    --hero-light: #b3d1ec;
    --band-blue: #7ab3d4;
    --band-green: #97c475;
    --state-blue: #0aa9e8;
    --button: #f0645a;
    --footer: #363b46;
    --device: #3a3d42;
    --map: #4f5b66;
  }
  * { box-sizing: border-box; margin: 0; padding: 0; }
  html, body { width: 1200px; height: 2618px; overflow: hidden; }
  body { position: relative; font-family: "Lato", Arial, sans-serif; color: var(--text); background: var(--white); }
  a { color: inherit; text-decoration: none; }

  /* top utility bar */
  .topbar { position: absolute; left: 0; top: 0; width: 1200px; height: 48px; background: var(--topbar); }
  .search-box { position: absolute; left: 150px; top: 11px; width: 232px; height: 30px; background: var(--white); border: 1px solid #ccc; }
  .search-box svg { position: absolute; left: 8px; top: 6px; }
  .social { position: absolute; left: 932px; top: 14px; display: flex; gap: 8px; }
  .social span { width: 20px; height: 20px; background: #333; border-radius: 2px; display: block; }

  /* header / navigation */
  .header { position: absolute; left: 0; top: 48px; width: 1200px; height: 118px; background: var(--white); }
  .logo { position: absolute; left: 196px; top: 44px; font-weight: 700; font-size: 38px; color: var(--text-dark); line-height: 1; letter-spacing: 1px; }
  .main-nav { position: absolute; top: 62px; left: 0; width: 1200px; font-size: 15px; color: var(--text-dark); }
  .main-nav a { position: absolute; top: 0; line-height: 28px; white-space: nowrap; }
  .main-nav .current { background: var(--nav-active); color: var(--white); padding: 0 10px; top: 0; }
  .main-nav .open { color: var(--brand-blue); }
  .caret { font-size: 10px; margin-left: 3px; opacity: .6; }

  .dropdown { position: absolute; left: 613px; top: 166px; width: 131px; height: 122px; background: var(--dropdown); padding: 18px 0 0 17px; z-index: 5; box-shadow: 0 2px 4px rgba(0,0,0,.15); }
  .dropdown li { list-style: none; font-size: 12.5px; line-height: 21px; color: var(--text-dark); }

  /* hero definition */
  .hero { position: absolute; left: 0; top: 166px; width: 1200px; height: 321px;
    background: linear-gradient(100deg, var(--hero-dark) 0%, #8fb6dc 40%, var(--hero-light) 70%, #7eaad6 100%); color: var(--white); font-family: "Tinos", "Times New Roman", serif; }
  .hero .word { position: absolute; left: 200px; top: 88px; font-size: 56px; font-weight: 700; letter-spacing: 3px; line-height: 1; }
  .hero .pron { position: absolute; left: 200px; top: 142px; font-size: 44px; line-height: 1; }
  .hero .pron i { font-style: italic; }
  .hero .senses { position: absolute; left: 637px; top: 54px; width: 520px; font-size: 15.5px; line-height: 19px; list-style: none; }
  .hero .senses li { padding-left: 19px; text-indent: -19px; }
  .hero .swoosh { position: absolute; left: 480px; top: 205px; }

  /* video */
  .video-intro { position: absolute; left: 0; top: 546px; width: 1200px; text-align: center; }
  .section-title { font-size: 37px; font-weight: 700; color: var(--brand-blue); line-height: 44px; }
  .video-intro p { width: 920px; margin: 36px auto 0; font-size: 16px; line-height: 21px; color: var(--text); }
  .device { position: absolute; left: 345px; top: 757px; width: 430px; height: 277px; background: var(--device); border-radius: 12px 12px 0 0; padding: 18px 20px 0; }
  .device-base { position: absolute; left: 275px; top: 1034px; width: 572px; height: 22px; background: linear-gradient(#c9c9c9, #8e8e8e); border-radius: 0 0 14px 14px; }
  .player { position: relative; width: 390px; height: 240px; background: linear-gradient(160deg, #c7a98a 0%, #8a7a6e 45%, #3c3c3c 100%); }
  .play-btn { position: absolute; left: 165px; top: 80px; }
  .controls { position: absolute; left: 0; bottom: 0; width: 390px; height: 22px; background: #f2f2f2; }
  .controls .track { position: absolute; left: 60px; top: 9px; width: 230px; height: 5px; background: #c8d7e4; }
  .controls .track i { display: block; width: 170px; height: 5px; background: var(--brand-blue); }
  .controls .time { position: absolute; left: 300px; top: 4px; font-size: 9px; color: #333; }
  .controls .hd { position: absolute; right: 8px; top: 4px; font-size: 10px; font-weight: 700; color: var(--brand-blue); }

  /* content bands */
  .band { position: absolute; left: 0; width: 1200px; }
  .band-blue { top: 1056px; height: 332px; background: var(--band-blue); color: var(--white); }
  .band-green { top: 1388px; height: 336px; background: var(--band-green); color: var(--white); }
  .band-white { top: 1724px; height: 344px; background: var(--white); }
  .band-title { position: absolute; left: 146px; font-size: 37px; font-weight: 700; line-height: 44px; }
  .band-white .band-title { color: var(--brand-blue); }
  .band-copy { position: absolute; left: 150px; font-size: 13.2px; line-height: 17.5px; }
  .band-copy p + p { margin-top: 17px; }
  .band-green .band-copy p + p { margin-top: 0; }
  .band-green .band-copy p.gap { margin-top: 17px; }
  .band-white .band-copy { color: var(--text-dark); }
  .read-more { position: absolute; left: 150px; width: 121px; height: 37px; background: var(--button); color: var(--white); font-size: 14px; line-height: 37px; text-align: center; text-transform: uppercase; }
  .band-shadow { position: absolute; left: 231px; bottom: -3px; width: 740px; height: 6px; background: #8f9497; opacity: .55; z-index: 2; border-radius: 0 0 50% 50%; }
  .world-map { position: absolute; left: 607px; top: 46px; width: 436px; height: 277px; background: radial-gradient(ellipse at 50% 45%, var(--map) 0%, #5c6c7a 55%, rgba(92,108,122,0) 75%); border-radius: 40px; }
  .people-chart { position: absolute; left: 640px; top: 98px; width: 370px; height: 153px; background: linear-gradient(#6b6b6b 0%, #6b6b6b 33%, #3aa3dc 33%, #3aa3dc 100%); opacity: .85; border-radius: 6px; }

  /* states */
  .states { position: absolute; left: 0; top: 2068px; width: 1200px; height: 358px; background: var(--state-blue); }
  .states-title { position: absolute; left: 301px; top: 42px; width: 594px; height: 68px; background: var(--white); border: 3px solid var(--white); outline: 2px solid var(--white); outline-offset: 4px; box-shadow: inset 0 0 0 2px var(--state-blue); text-align: center; font-size: 35px; font-weight: 700; line-height: 62px; color: var(--brand-blue); }
  .state-col { position: absolute; top: 150px; list-style: none; }
  .state-col li { font-size: 16px; line-height: 34.5px; font-weight: 700; font-style: italic; color: var(--white); text-decoration: underline; }

  /* footer */
  .footer { position: absolute; left: 0; top: 2426px; width: 1200px; height: 192px; background: var(--footer); color: var(--white); text-align: center; }
  .footer .logo-foot { margin-top: 46px; font-size: 38px; font-weight: 700; line-height: 1; }
  .footer .links { margin-top: 16px; font-size: 14px; }
  .footer .links span { margin: 0 10px; }
  .footer .url { margin-top: 22px; font-size: 13px; }
</style>
</head>
<body>

<div class="topbar">
  <div class="search-box">
    <svg width="18" height="18" viewBox="0 0 18 18"><circle cx="7" cy="7" r="5" fill="none" stroke="#1e5a8a" stroke-width="2"/><line x1="11" y1="11" x2="16" y2="16" stroke="#1e5a8a" stroke-width="2.5"/></svg>
  </div>
  <div class="social" aria-label="Social links"><span></span><span></span><span></span><span></span></div>
</div>

<header class="header">
  <div class="logo">LOGO</div>
  <nav class="main-nav">
    <a class="current" style="left:375px">Home</a>
    <a style="left:450px">States<span class="caret">&#8964;</span></a>
    <a style="left:528px">Programs<span class="caret">&#8964;</span></a>
    <a class="open" style="left:631px">Degrees<span class="caret">&#8964;</span></a>
    <a style="left:724px">Accreditation</a>
    <a style="left:851px">Rankings</a>
    <a style="left:951px">Resources</a>
  </nav>
</header>

<ul class="dropdown">
  <li>Certificate</li><li>Associate</li><li>Bachelors</li><li>Masters</li><li>PhD</li>
</ul>

<section class="hero">
  <div class="word">ac·cred·it·ed</div>
  <div class="pron">[uh-kred-i-tid] <i>adj.</i></div>
  <ol class="senses">
    <li>1. officially recognized as meeting the essential requirements, as of academic excellence: accredited schools.</li>
    <li>2. provided with official credentials, as by a government: an accredited diplomatic representative.</li>
    <li>3. accepted as authoritative: an accredited theory.</li>
  </ol>
  <svg class="swoosh" width="190" height="60" viewBox="0 0 190 60"><path d="M8 44 Q80 70 175 18" fill="none" stroke="#fff" stroke-width="3" stroke-linecap="round"/><path d="M160 14 L178 16 L170 32" fill="none" stroke="#fff" stroke-width="3" stroke-linecap="round" stroke-linejoin="round"/></svg>
</section>

<section class="video-intro">
  <h2 class="section-title">WATCH OUR VIDEO</h2>
  <p>Lorem ipsum dolor sit amet, consectetur adipiscing elit. Fusce rutrum magna in nisi mattis, ut mollis lorem dictum. Morbi ac condimentum lacus. Phasellus dolor magna, rhoncus et interdum eget, tempor non sapien. Nullam fermentum ultrices ipsum non molestie. Nunc vitae nulla ut felis ultrices mollis nec vel felis. Sed vehicula orci a orci vehicula mattis. Cum sociis natoque penatibus et magnis dis parturient montes, nascetur ridiculus mus.</p>
</section>

<div class="device">
  <div class="player" role="img" aria-label="Video still of a presenter speaking to camera">
    <svg class="play-btn" width="60" height="60" viewBox="0 0 60 60"><circle cx="30" cy="30" r="26" fill="rgba(255,255,255,.25)" stroke="#fff" stroke-width="3"/><path d="M23 17 L43 30 L23 43 Z" fill="#fff"/></svg>
    <div class="controls">
      <svg width="44" height="22" viewBox="0 0 44 22"><path d="M8 6 L15 11 L8 16 Z" fill="#333"/><path d="M26 9 h3 l4 -3 v10 l-4 -3 h-3 z" fill="#888"/></svg>
      <div class="track"><i></i></div>
      <div class="time">2:45 / 3:12</div>
      <div class="hd">HD</div>
    </div>
  </div>
</div>
<div class="device-base"></div>

<section class="band band-blue">
  <h2 class="band-title" style="top:48px">Header Title 1</h2>
  <div class="band-copy" style="top:107px;width:440px">
    <p>Lorem ipsum dolor sit amet, consectetur adipiscing elit. Fusce rutrum magna in nisi mattis, ut mollis lorem dictum. Morbi ac condimentum lacus. Phasellus dolor magna, rhoncus et interdum eget, tempor non sapien.</p>
    <p>Nunc vitae nulla ut felis ultrices mollis nec vel felis. Sed vehicula orci a orci vehicula mattis. Cum sociis natoque penatibus et magnis dis parturient montes, nascetur ridiculus mus. Nulla ullamcorper risus eu justo pellentesque</p>
  </div>
  <a class="read-more" style="top:253px">Readmore</a>
  <div class="world-map" role="img" aria-label="World map with location markers"></div>
  <div class="band-shadow"></div>
</section>

<section class="band band-green">
  <h2 class="band-title" style="top:48px">Header Title 2</h2>
  <div class="band-copy" style="top:108px;width:940px">
    <p>Lorem ipsum dolor sit amet, consectetur adipiscing elit. Fusce rutrum magna in nisi mattis, ut mollis lorem dictum. Morbi ac condimentum lacus. Phasellus dolor magna, rhoncus et interdum eget, tempor non sapien. Nullam fermentum ultrices ipsum non molestie.</p>
    <p>Nunc vitae nulla ut felis ultrices mollis nec vel felis. Sed vehicula orci a orci vehicula mattis. Cum sociis natoque penatibus et magnis dis parturient montes, nascetur ridiculus mus. Nulla ullamcorper risus eu justo pellentesque consequat.</p>
    <p class="gap">Phasellus a convallis dui, id laoreet turpis. Cras condimentum odio sed gravida accumsan. Proin posuere vitae erat id convallis. Cras tempus, elit eget condimentum pretium, lacus nisl rhoncus neque, ac semper justo purus vel lacus. Mauris scelerisque lobortis quam sit amet tristique. Sed ullamcorper molestie</p>
  </div>
  <a class="read-more" style="top:255px">Readmore</a>
  <div class="band-shadow"></div>
</section>

<section class="band band-white">
  <h2 class="band-title" style="top:52px">Header Title 3</h2>
  <div class="band-copy" style="top:116px;width:440px">
    <p>Lorem ipsum dolor sit amet, consectetur adipiscing elit. Fusce rutrum magna in nisi mattis, ut mollis lorem dictum. Morbi ac condimentum lacus. Phasellus dolor magna, rhoncus et interdum eget, tempor non sapien. Nullam fermentum ultrices ipsum non molestie.<br>Nunc vitae nulla ut felis ultrices mollis nec vel felis. Sed vehicula orci a orci vehicula mattis. Cum sociis natoque penatibus et magnis dis parturient montes, nascetur ridiculus mus. Nulla ullamcorper risus eu justo pellentesque</p>
  </div>
  <a class="read-more" style="top:259px">Readmore</a>
  <div class="people-chart" role="img" aria-label="Figure chart of people, one row grey and two rows blue, grouped by a bracket"></div>
</section>

<section class="states">
  <h2 class="states-title">Search Colleges by State</h2>
  <ul class="state-col" style="left:168px"><li>California</li><li>Texas</li><li>Illinois</li><li>Virginia</li><li>Massachusetts</li></ul>
  <ul class="state-col" style="left:321px"><li>Kentucky</li><li>Florida</li><li>New Jersy</li><li>Pennsylvania</li><li>Alaska</li></ul>
  <ul class="state-col" style="left:478px"><li>Louisiana</li><li>Arizona</li><li>Georgia</li><li>Tennessee</li><li>Colorado</li></ul>
  <ul class="state-col" style="left:626px"><li>California</li><li>Texas</li><li>Illinois</li><li>Virginia</li><li>Massachusetts</li></ul>
  <ul class="state-col" style="left:779px"><li>Kentucky</li><li>Florida</li><li>New Jersy</li><li>Pennsylvania</li><li>Alaska</li></ul>
  <ul class="state-col" style="left:936px"><li>Louisiana</li><li>Arizona</li><li>Georgia</li><li>Tennessee</li><li>Colorado</li></ul>
</section>

<footer class="footer">
  <div class="logo-foot">LOGO</div>
  <div class="links">about us<span>|</span>privacy<span>|</span>copyright</div>
  <div class="url">www.url.com</div>
</footer>

</body>
</html>
```